High-End Medical Center Website Design Project

This design is part of a well thought-out project by an experienced project manager / developer. The approved wireframe is attached. Creative interpretations / suggestions based on the layout encouraged.

The design is for a new state-of-the-art medical center located in Dallas, Texas. The target audience would likely be individuals (approx. 60% female /40% male) who are the healthcare decision-makers for their families. They would likely have insurance and be inclined to seek out top-quality care.

Potential clients would choose this client over others in their industry because the medical center is physician owned, meaning it is patient-focused rather than profit-focused. The facility is brand new, featuring the latest technology. (This includes an amazing waiting room featuring WiFi and docking stations.) The physicians are hand-picked by referral only.

The look of the site should be extremely clean. We are going for a well-organized, professional look with a bit of a warm glow (interpret that however you like). Use crisp corners and the colors in the logo.

Think modern, clean with some great use of color / font.

We can get lovely photography of the medical center once construction is complete. Feel free to use an "example image" behind the Featured Area ("Physician Owned. Patient-Focused") if you like. We are open to ideas.

ONE CHANGE REQUESTED IN THE WIREFRAME:

Remove the "Connect" 1/4 page footer area and replace with a quick contact form. You may swap the "Locations" area with the form if desired. Put social media icons at the top left of the page in the top header area.

(Note: Please use social media icons that match the design rather than standard icons. We preferred not placing the icons at the top, but the client requested this. Let's not bring more attention to them than necessary.)
Updates

We're custom programming this site, so there's no need to base it on a template. Also, we would prefer not to use typical "seen everywhere" stock images.Thanks.

Industry/Entity Type

Construction

Requirements
Must have
• Follow the wireframe. This has been approved.
Nice to have
• Examples of what hover states, links or dropdowns might look like.

```html
<!DOCTYPE html>
<html lang="en">
<head>
<meta charset="utf-8">
<title>Lumen Medical Center</title>
<link href="https://fonts.googleapis.com/css2?family=Open+Sans:wght@400;600;700&display=swap" rel="stylesheet">
<style>
:root{
  --navy:#0c50a3;
  --teal:#3ea7b5;
  --teal-dark:#2f95a3;
  --ink:#222;
  --muted:#555;
  --grey-bg:#f4f4f4;
  --mint:#d3eef1;
  --orange:#e8691e;
  --white:#fff;
}
*{box-sizing:border-box;margin:0;padding:0}
html,body{width:792px;height:1200px;overflow:hidden;background:var(--white)}
body{position:relative;font-family:"Open Sans",Arial,sans-serif;color:var(--ink)}
.abs{position:absolute}
a{color:inherit;text-decoration:none}

.topbar{left:0;top:0;width:792px;height:26px;background:var(--navy)}
.social{left:78px;top:7px;display:flex;gap:9px}
.social span{width:12px;height:12px;border-radius:50%;background:#fff;opacity:.85;display:block}
.phone{right:72px;top:3px;color:#fff;font-size:14px;display:flex;align-items:center;gap:10px}

.header{left:0;top:26px;width:792px;height:63px;background:#fff;border-bottom:1px solid #e6e6e6}
.brand{left:78px;top:15px;display:flex;align-items:center;gap:8px}
.brand-mark{width:22px;height:22px;background:var(--navy)}
.brand-name{font-size:19px;font-weight:700;color:var(--navy);letter-spacing:.5px}
.nav{left:366px;top:38px;display:flex;gap:22px;font-size:9.5px;color:#444;letter-spacing:.3px}
.nav a.active{color:var(--teal)}

.hero{left:0;top:89px;width:792px;height:285px;background:linear-gradient(90deg,#eef3f6 0%,#e3ebf0 45%,#dfe8ee 75%,#eef3f6 100%)}
.hero-photo{left:396px;top:0;width:300px;height:285px;background:linear-gradient(180deg,#e9eef2,#cfd9e1)}
.hero-title{left:89px;top:106px;font-size:28px;font-weight:600;line-height:35px;letter-spacing:.3px}
.hero-title .l1{color:var(--teal)}
.hero-title .l2{color:var(--navy);display:block;padding-left:6px}
.dots{left:80px;top:255px;display:flex;gap:9px}
.dots span{width:12px;height:12px;border-radius:50%;background:#b9c4ca}
.dots span.on{background:var(--teal)}

.tour{left:0;top:374px;width:792px;height:59px;background:#fff}
.tour-text{left:262px;top:18px;font-size:18px;color:var(--teal-dark)}
.btn-lg{left:428px;top:16px;width:147px;height:27px;background:var(--teal);color:#fff;font-size:10px;display:flex;align-items:center;justify-content:center}

.apart{left:0;top:433px;width:792px;height:346px;background:var(--grey-bg);border-top:1px solid #e8e8e8}
.apart-title{left:0;top:14px;width:784px;text-align:center;font-size:14px;color:var(--teal-dark)}
.apart-rule{left:108px;top:42px;width:576px;height:1px;background:#dedede}
.feature{top:74px;width:170px;text-align:left}
.feature .icon{width:79px;height:79px;border-radius:50%;background:var(--teal);margin:0 auto;display:flex;align-items:center;justify-content:center}
.feature h3{font-weight:400;font-size:14px;color:var(--teal-dark);text-align:center;margin-top:13px}
.feature p{font-size:8.3px;line-height:13.2px;color:#333;margin-top:9px;padding-left:6px}
.feature .more{display:block;text-align:right;font-size:8px;font-style:italic;color:var(--orange);margin-top:32px;padding-right:18px}

.story{left:0;top:779px;width:792px;height:200px;background:#fff}
.doctor-photo{left:84px;top:24px;width:127px;height:150px;background:linear-gradient(180deg,#e9eef1,#cdd7de)}
.story h2{left:222px;top:36px;font-size:14px;font-weight:400;color:var(--navy)}
.story p.body{left:222px;top:64px;width:315px;font-size:8.3px;line-height:14.3px;color:#333}
.btn-sm{height:15px;width:61px;background:var(--teal);color:#fff;font-size:8px;display:flex;align-items:center;justify-content:center}
.story h2.testi{left:581px;color:var(--navy)}
.quote{left:581px;top:64px;width:150px;font-size:8.3px;line-height:14.3px;color:#333}
.quote b{color:var(--teal);font-size:20px;font-style:italic;line-height:0;vertical-align:-6px}

.footer{left:0;top:979px;width:792px;height:176px;background:var(--mint)}
.ft-h{font-size:14px;color:var(--teal-dark);display:flex;align-items:center;gap:6px}
.news h4{font-size:11px;font-weight:400;color:#222;margin-top:4px}
.news p{font-size:7.4px;line-height:10.5px;color:#666}
.news .date{font-size:7.4px;color:var(--navy);margin-bottom:8px}
.loc p{font-size:7.4px;line-height:10.6px;color:#444}
.loc .mail{color:var(--navy)}
.field{width:137px;height:14px;background:#fff;border:1px solid #9fd3da;font-size:7px;color:#888;padding:2px 6px;margin-bottom:7px}
.field.area{height:50px}
.wait{font-size:14px;color:#444;text-align:center;width:150px}
.small{font-size:7px;line-height:11px;color:#555}
.news-form{display:flex}
.news-form .field{width:103px;margin:0}
.news-form .btn-sm{width:36px;height:14px}

.bottombar{left:0;top:1155px;width:792px;height:45px;background:var(--navy);color:#fff;font-size:7px;font-weight:700}
</style>
</head>
<body>

<div class="abs topbar">
  <div class="abs social" aria-label="Social links"><span></span><span></span><span></span><span></span></div>
  <div class="abs phone">
    <svg width="18" height="18" viewBox="0 0 18 18"><circle cx="9" cy="9" r="8" fill="none" stroke="#fff" stroke-width="1.5"/><path d="M6 5c-1 1-1 3 1 5s4 2.5 5 1.5l-1.5-1.5-1 .5c-.7-.3-1.7-1.3-2-2l.5-1z" fill="#fff"/></svg>
    (214) 555 0147
  </div>
</div>

<header class="abs header">
  <div class="abs brand"><span class="brand-mark"></span><span class="brand-name">LUMEN MEDICAL CENTER</span></div>
  <nav class="abs nav">
    <a class="active" href="#">WHY LUMEN</a><a href="#">PHYSICIANS</a><a href="#">SPECIALTIES</a><a href="#">LOCATIONS</a><a href="#">CONTACT</a>
  </nav>
</header>

<section class="abs hero">
  <div class="abs hero-photo" role="img" aria-label="Smiling female physician in white coat holding a clipboard in a bright clinic"></div>
  <h1 class="abs hero-title"><span class="l1">PHYSICIAN OWNED</span><span class="l2">PATIENT FOCUSED</span></h1>
  <div class="abs dots"><span class="on"></span><span></span><span></span></div>
</section>

<section class="abs tour">
  <div class="abs tour-text">Take a virtual tour</div>
  <a class="abs btn-lg" href="#">Click Here to Start</a>
</section>

<section class="abs apart">
  <h2 class="abs apart-title" style="font-weight:400">What sets us apart</h2>
  <div class="abs apart-rule"></div>

  <div class="abs feature" style="left:70px">
    <div class="icon"><svg width="46" height="46" viewBox="0 0 46 46" fill="none" stroke="#fff" stroke-width="3"><path d="M30 6v10a8 8 0 0 1-16 0"/><path d="M22 24v6a8 8 0 0 1-8 8"/><circle cx="12" cy="36" r="5"/></svg></div>
    <h3>Physician Owned</h3>
    <p>Lorem ipsum dolor sit amet, consetetur sadipscing elitr, sed diam nonumy eirmod tempor invidunt ut labore et dolore magna aliquyam erat, sed diam voluptua.</p>
    <a class="more" href="#">Read more →</a>
  </div>
  <div class="abs feature" style="left:236px">
    <div class="icon"><svg width="46" height="46" viewBox="0 0 46 46" fill="#fff"><path d="M20 6h8v12h-8z"/><path d="M14 18a14 14 0 0 0 14 20h12v-5H28a9 9 0 0 1-9-15z"/><rect x="10" y="38" width="30" height="4"/></svg></div>
    <h3>Technology</h3>
    <p>Lorem ipsum dolor sit amet, consetetur sadipscing elitr, sed diam nonumy eirmod tempor invidunt ut labore et dolore magna aliquyam erat, sed diam voluptua.</p>
    <a class="more" href="#">Read more →</a>
  </div>
  <div class="abs feature" style="left:404px">
    <div class="icon"><svg width="46" height="46" viewBox="0 0 46 46" fill="#fff"><circle cx="18" cy="10" r="5"/><rect x="11" y="17" width="14" height="22" rx="3"/><circle cx="32" cy="18" r="4"/><rect x="27" y="24" width="10" height="15" rx="3"/></svg></div>
    <h3>Quality of Care</h3>
    <p>Lorem ipsum dolor sit amet, consetetur sadipscing elitr, sed diam nonumy eirmod tempor invidunt ut labore et dolore magna aliquyam erat, sed diam voluptua.</p>
    <a class="more" href="#">Read more →</a>
  </div>
  <div class="abs feature" style="left:569px">
    <div class="icon"><svg width="50" height="46" viewBox="0 0 50 46"><path d="M23 40C6 28 4 20 4 14a9 9 0 0 1 19-4 9 9 0 0 1 19 4c0 6-2 14-19 26z" fill="#fff"/><circle cx="36" cy="32" r="9" fill="var(--teal)" stroke="#fff" stroke-width="2.5"/><path d="M36 27v10M31 32h10" stroke="#fff" stroke-width="2.5"/></svg></div>
    <h3>Patient Experience</h3>
    <p>Lorem ipsum dolor sit amet, consetetur sadipscing elitr, sed diam nonumy eirmod tempor invidunt ut labore et dolore magna aliquyam erat, sed diam voluptua.</p>
    <a class="more" href="#">Read more →</a>
  </div>
</section>

<section class="abs story">
  <div class="abs doctor-photo" role="img" aria-label="Male physician in white coat writing on a tablet"></div>
  <h2 class="abs">Lorem Ipsum Heading</h2>
  <p class="abs body">Lorem ipsum dolor sit amet, consetetur sadipscing elitr, sed diam nonumy eirmod tempor invidunt ut labore et dolore magna aliquyam erat, sed diam voluptua. At vero eos et accusam et justo duo dolores et ea rebum. Stet clita kasd gubergren, no sea takimata sanctus est Lorem ipsum dolor sit amet. At vero eos et accusam et justo duo dolores et ea rebum.</p>
  <a class="abs btn-sm" href="#" style="left:223px;top:155px">Read More</a>

  <h2 class="abs testi">Testimonials</h2>
  <p class="abs quote"><b>//</b> Lorem ipsum dolor sit amet, consetetur sadipscing elitr, sed diam nonumy eirmod tempor invidunt ut labore et dolore magna aliquyam erat, sed diam voluptua. <b>//</b></p>
  <a class="abs btn-sm" href="#" style="left:582px;top:155px">Read More</a>
</section>

<footer class="abs footer">
  <div class="abs news" style="left:77px;top:16px;width:145px">
    <div class="ft-h">Latest news</div>
    <h4>Lorem Ipsum Heading</h4>
    <p>Lorem ipsum dolor sit amet, consectetuer a iscing elit. Aenean commodo ligula eget dolo. Aenean commodo.</p>
    <p class="date">September 1th, 2013</p>
    <h4>Lorem Ipsum Heading</h4>
    <p>Lorem ipsum dolor sit amet, consectetuer a iscing elit. Aenean commodo ligula eget dolo. Aenean commodo.</p>
    <p class="date">September 1th, 2013</p>
  </div>

  <div class="abs loc" style="left:248px;top:12px;width:140px">
    <div class="ft-h"><svg width="18" height="22" viewBox="0 0 18 22"><path d="M9 1a8 8 0 0 1 8 8c0 5-8 12-8 12S1 14 1 9a8 8 0 0 1 8-8z" fill="var(--teal)"/><circle cx="9" cy="9" r="3" fill="var(--mint)"/></svg>Locations</div>
    <div style="margin:7px 0 0 10px">
      <p>48 Cedar Row, Dallas, Texas</p><p>Phone: (214) 555 0199</p><p>Fax: (214) 555 0199</p><p class="mail">hello@lumenmedical.org</p>
      <p style="margin-top:13px">48 Cedar Row, Dallas, Texas</p><p>Phone: (214) 555 0199</p><p>Fax: (214) 555 0199</p><p class="mail">hello@lumenmedical.org</p>
    </div>
  </div>

  <div class="abs" style="left:401px;top:15px">
    <div class="ft-h"><svg width="24" height="16" viewBox="0 0 24 16"><rect x="1" y="3" width="22" height="12" fill="var(--teal)"/><path d="M1 3l11 7 11-7" fill="none" stroke="var(--mint)" stroke-width="1.5"/></svg>Contact Us</div>
    <div style="margin-top:6px">
      <div class="field">Your name</div>
      <div class="field">Your email address</div>
      <div class="field area">Your message</div>
      <a class="btn-sm" href="#" style="margin-top:2px">Send</a>
    </div>
  </div>

  <div class="abs" style="left:582px;top:12px;width:160px">
    <div class="ft-h"><svg width="20" height="20" viewBox="0 0 20 20"><circle cx="10" cy="10" r="8.5" fill="none" stroke="var(--teal)" stroke-width="2"/><path d="M10 10V4a6 6 0 1 1-6 6z" fill="var(--teal)"/></svg>Average Wait Time</div>
    <div class="wait" style="margin-top:8px">9 min</div>
    <p class="small" style="margin-top:9px">Cum sociis natoque penatibus et<br>magnis dis parturient montes, nascetur.</p>
    <div class="ft-h" style="margin-top:18px">Sign up for Newsletter</div>
    <div class="news-form" style="margin-top:8px"><div class="field">Your email address</div><a class="btn-sm" href="#">Send</a></div>
  </div>
</footer>

<div class="abs bottombar">
  <span class="abs" style="left:77px;top:14px">© 2013 All Right Reserved</span>
  <a class="abs" href="#" style="left:586px;top:14px;font-weight:400;text-decoration:underline">Back to top</a>
</div>

</body>
</html>
```